Design some Business Cards

Need some business cards made for new venture - website is vantrimo.com. I want to incorporate (in some fashion):

- logo (provided with name, and alone)
- website <p> font (Arvo )

Brian T. Holloway
BH VANTRIMO
817 E. Thornbury Ave. 3rd Floor
Chicago, IL 60648
brianh@vantrimo.com
(312) 555-0148
vantrimo.com

I am not very creative, hence the contest. Feel free to add design elements, but keep things consistent with the website (naturally). I am indifferent to one side vs. two-sided business card. I will be using CardNexa, so you will want to use their Illustrator (or photoshop) templates located here:

http://www.cardnexa-print.com/cn/ns/prodesk/UploadFiles.aspx?pf_id=Q41&selectedTab=0

The work product will be an Illustrator or Photoshop file, using the templates, with the winning design.

```html
<!DOCTYPE html>
<html lang="en">
<head>
<meta charset="utf-8">
<title>Vantrimo Business Cards</title>
<link rel="stylesheet" href="https://fonts.googleapis.com/css2?family=Arvo:wght@400;700&family=Open+Sans:ital,wght@0,400;0,600;1,600&display=swap">
<style>
  :root {
    --stage: #d6d6d8;
    --card-dark: #1f1f21;
    --tab-dark: #2b2326;
    --silver-light: #f6f6f6;
    --silver-mid: #d2d2d4;
    --strip-gray: #a3a3a5;
    --ink: #242426;
    --ink-soft: #4a4a4c;
    --paper-text: #e4e4e6;
    --rule: #8a8a8c;
  }
  * { margin: 0; padding: 0; box-sizing: border-box; }
  html, body { width: 1200px; height: 864px; overflow: hidden; }
  body { background: var(--stage); position: relative; font-family: "Open Sans", sans-serif; }

  .card { position: absolute; border-radius: 6px; overflow: hidden; box-shadow: 0 10px 30px rgba(0,0,0,.28); }
  .card-shape { position: absolute; inset: 0; width: 100%; height: 100%; display: block; }

  /* Back side */
  .card-back { left: 600px; top: 70px; width: 540px; height: 308px; background: var(--card-dark); }
  .card-back .brand { position: absolute; left: 150px; top: 150px; }

  /* Brand lockup */
  .brand { display: flex; align-items: center; gap: 12px; }
  .brand-dot { width: 24px; height: 24px; border-radius: 50%; }
  .brand-name { font-family: "Arvo", serif; font-weight: 700; line-height: 1; }
  .card-back .brand-dot { background: var(--paper-text); }
  .card-back .brand-name { color: var(--paper-text); font-size: 40px; }

  /* Front side */
  .card-front { left: 60px; top: 450px; width: 620px; height: 354px; }
  .card-front .brand { position: absolute; left: 36px; top: 36px; }
  .card-front .brand-dot { background: var(--ink); }
  .card-front .brand-name { color: var(--ink); font-size: 40px; }

  .holder { position: absolute; left: 316px; top: 96px; height: 28px; display: flex; align-items: center; gap: 10px; }
  .holder-name { font-weight: 600; font-style: italic; font-size: 17px; color: var(--ink); }
  .holder-title { font-size: 10px; letter-spacing: .5px; color: var(--ink-soft); border-left: 1px solid var(--ink-soft); padding-left: 8px; }

  .contact { position: absolute; top: 168px; display: flex; gap: 14px; color: var(--paper-text); font-size: 13px; line-height: 1.45; }
  .address { width: 270px; text-align: right; padding-top: 2px; }
  .contact-rule { width: 1px; height: 58px; background: var(--rule); }
  .reach { padding-top: 16px; }
  .contact { left: 40px; }

  .web { position: absolute; left: 44px; top: 302px; font-size: 13px; color: var(--ink); font-family: "Arvo", serif; }
</style>
</head>
<body>

  <section class="card card-back" aria-label="Card back">
    <div class="brand">
      <span class="brand-dot"></span>
      <span class="brand-name">vantrimo</span>
    </div>
  </section>

  <section class="card card-front" aria-label="Card front">
    <svg class="card-shape" viewBox="0 0 620 354" aria-hidden="true">
      <defs>
        <linearGradient id="silver" x1="0" y1="0" x2="1" y2="0">
          <stop offset="0" stop-color="var(--silver-light)"/>
          <stop offset="1" stop-color="var(--silver-mid)"/>
        </linearGradient>
      </defs>
      <rect width="620" height="354" fill="var(--card-dark)"/>
      <rect x="470" y="0" width="150" height="40" fill="var(--tab-dark)"/>
      <path d="M0 0 H478 Q492 0 500 12 Q508 26 528 26 H620 V124 H0 Z" fill="url(#silver)"/>
      <path d="M300 96 H620 V124 H290 Z" fill="var(--strip-gray)"/>
      <path d="M0 292 H196 Q222 292 224 318 V330 H0 Z" fill="url(#silver)"/>
    </svg>

    <div class="brand">
      <span class="brand-dot"></span>
      <span class="brand-name">vantrimo</span>
    </div>

    <div class="holder">
      <span class="holder-name">Brian T. Holloway</span>
      <span class="holder-title">BH VANTRIMO</span>
    </div>

    <div class="contact">
      <p class="address">817 E. Thornbury Ave. 3rd Floor,<br>Chicago, IL 60648</p>
      <span class="contact-rule"></span>
      <p class="reach">brianh@vantrimo.com<br>(312) 555-0148</p>
    </div>

    <p class="web">vantrimo.com</p>
  </section>

</body>
</html>
```